Motor Oil Lubricant Package Labels

We are looking for a logo and label that we can put on our motor oil bottle 1 liter and 5 liter. The name of our motor oil is Quentora. We want to design our flagship logo for QUENTORA MOTOR OILS and as well as the label that will go on the bottle. We have some drafts that we have come up with attached and would like to see more options. The concept of a timeless motor oil and the endless loop of lubricating oils incorporated in the design. We will have full synthetic motor oil, a synthetic blend motor, ATF III transmission fluid, KOR-II transmission fluid. hydraulic oils etc. Examples will be attached
Target Market(s)
Automotive Lubricants and Chemicals
Industry/Entity Type
Automotive
Logo Text
Quentora Lubricants
Other font styles liked:
- Let designer choose
Requirements
Must have
- The Quentora sign incorporated in a very cool way to our name. Our brand needs to stick out
Nice to have
- Automotive lubricant related and colors red, white, and blue incorporated in the design
Should not have
- Images of individuals and or topics not related to automotive lubricants.

```html
<!DOCTYPE html>
<html lang="en">
<head>
<meta charset="utf-8">
<title>Quentora Motor Oil Labels</title>
<link href="https://fonts.googleapis.com/css2?family=Oswald:wght@500;700&family=Poppins:wght@800&display=swap" rel="stylesheet">
<style>
  :root {
    --bg: #e9e9ea;
    --paper: #ffffff;
    --brand-blue: #1b3aa0;
    --blue-light: #2c4fc0;
    --brand-red: #e8000f;
    --ink: #111111;
    --silver-dark: #8f9398;
    --silver-light: #f2f2f3;
    --gold: #c9962f;
    --edge: #b8b8bb;
  }
  * { margin: 0; padding: 0; box-sizing: border-box; }
  html, body { width: 1200px; height: 935px; overflow: hidden; }
  body {
    background: radial-gradient(ellipse at center, #f6f6f7 0%, var(--bg) 75%);
    font-family: "Oswald", sans-serif;
    position: relative;
  }
  .label {
    position: absolute;
    top: 116px;
    width: 432px;
    height: 702px;
    border-radius: 32px;
    overflow: hidden;
    background: var(--paper);
    border: 1px solid var(--edge);
  }
  .label--front { left: 142px; }
  .label--back { left: 626px; }
  .label__art { position: absolute; inset: 0; width: 100%; height: 100%; }
  .brand-name {
    position: absolute;
    transform: translateX(-50%);
    font-family: "Poppins", sans-serif;
    font-weight: 800;
    font-size: 54px;
    color: var(--ink);
    letter-spacing: -1px;
    white-space: nowrap;
  }
  .label--front .brand-name { left: 197px; top: 140px; }
  .label--back .brand-name { left: 218px; top: 104px; }
  .grade {
    position: absolute;
    transform: translate(-50%, -50%) rotate(-90deg);
    color: var(--paper);
    white-space: nowrap;
    line-height: 1;
  }
  .label--front .grade { left: 330px; top: 476px; }
  .label--back .grade { left: 346px; top: 480px; }
  .grade__type {
    display: block;
    font-weight: 700;
    font-size: 21px;
    letter-spacing: 2px;
    margin-bottom: 2px;
  }
  .grade__main { display: flex; align-items: baseline; gap: 6px; font-weight: 700; }
  .grade__sae { font-size: 30px; }
  .grade__visc { font-size: 62px; letter-spacing: 1px; }
  .grade__api { font-size: 34px; margin-left: 8px; }
  .seal {
    position: absolute;
    left: 40px; top: 338px;
    width: 112px; height: 112px;
    border-radius: 50%;
    background: radial-gradient(circle at 35% 30%, #f7dc8a, var(--gold) 60%, #8a5f16);
    display: flex; align-items: center; justify-content: center;
  }
  .seal__inner {
    width: 78px; height: 78px; border-radius: 50%;
    background: var(--paper);
    display: flex; align-items: center; justify-content: center;
    text-align: center;
    font-weight: 500; font-size: 12px; line-height: 1.35;
    color: var(--ink);
  }
  .volume {
    position: absolute; left: 41px; top: 651px;
    font-weight: 700; font-size: 21px; color: var(--ink);
  }
  .origin-note {
    position: absolute; left: 260px; top: 653px;
    font-weight: 500; font-size: 16px; color: var(--paper);
  }
  .flag {
    position: absolute; left: 46px; top: 546px;
    width: 93px; height: 48px;
    background: linear-gradient(180deg, #c8102e 0%, #e8e8ea 50%, #c8102e 100%);
  }
  .flag::before {
    content: ""; position: absolute; left: 0; top: 0;
    width: 38px; height: 26px; background: #1f2f6b;
  }
  .flag-caption {
    position: absolute; left: 50px; top: 598px;
    font-family: Arial, sans-serif; font-size: 12px; letter-spacing: 1px; color: var(--ink);
  }
</style>
</head>
<body>

<section class="label label--front">
  <svg class="label__art" viewBox="0 0 432 702" aria-hidden="true">
    <defs>
      <linearGradient id="silverFront" x1="0" y1="0" x2="1" y2="1">
        <stop offset="0" stop-color="var(--silver-light)"/>
        <stop offset="0.5" stop-color="var(--silver-dark)"/>
        <stop offset="1" stop-color="var(--silver-light)"/>
      </linearGradient>
    </defs>
    <path d="M0 0 H242 C130 50 40 140 0 252 Z" fill="var(--brand-blue)"/>
    <path d="M190 0 H222 C120 52 40 140 0 240 V215 C40 120 110 45 190 0 Z" fill="var(--blue-light)"/>
    <path d="M432 176 C300 215 200 340 168 702 H200 C230 360 320 240 432 188 Z" fill="url(#silverFront)"/>
    <path d="M432 188 C320 240 230 360 200 702 H432 Z" fill="var(--brand-red)"/>
  </svg>
  <div class="brand-name">Quentora</div>
  <div class="seal"><div class="seal__inner">FOR<br>GASOLINE<br>ENGIENS</div></div>
  <div class="grade">
    <span class="grade__type">SYNTHETIC BLEND</span>
    <span class="grade__main"><span class="grade__sae">SAE</span><span class="grade__visc">5W-30</span><span class="grade__api">APISN</span></span>
  </div>
  <div class="volume">32oz 1946 mU</div>
  <div class="origin-note">Made In USA</div>
</section>

<section class="label label--back">
  <svg class="label__art" viewBox="0 0 432 702" aria-hidden="true">
    <defs>
      <linearGradient id="silverBack" x1="0" y1="0" x2="1" y2="1">
        <stop offset="0" stop-color="var(--silver-light)"/>
        <stop offset="0.5" stop-color="var(--silver-dark)"/>
        <stop offset="1" stop-color="var(--silver-light)"/>
      </linearGradient>
    </defs>
    <path d="M0 0 H242 C130 50 40 140 0 252 Z" fill="var(--brand-blue)"/>
    <path d="M190 0 H222 C120 52 40 140 0 240 V215 C40 120 110 45 190 0 Z" fill="var(--blue-light)"/>
    <path d="M432 184 C320 225 225 350 192 702 H224 C252 370 340 250 432 196 Z" fill="url(#silverBack)"/>
    <path d="M432 196 C340 250 252 370 224 702 H432 Z" fill="var(--brand-red)"/>
  </svg>
  <div class="brand-name">Quentora</div>
  <div class="flag" role="img" aria-label="United States flag"></div>
  <div class="flag-caption">MADE IN USA</div>
  <div class="grade">
    <span class="grade__type">SYNTHETIC BLEND</span>
    <span class="grade__main"><span class="grade__sae">SAE</span><span class="grade__visc">5W-30</span><span class="grade__api">APISN</span></span>
  </div>
</section>

</body>
</html>
```